Center for Cellular Datacraft wordpress design

We need a wordpress design for the new Center for Cellular Datacraft at the Halvorsen State College. We are a research institute focused on medical and biological research involving big data and informatics. The website has to be eyecatching and appropriate for an academic context, with easily updated content.

Press release here: http://www.hscmed.halvorsen.edu/news/News_Releases/2013/02/cellular/

We would prefer to use images from our research labs over stock art, but feel free to use placeholders for now. Please contact me if there are specific types of images you need.

Target Market(s)

Tech-savvy academics, faculty, students, general laypeople

Industry/Entity Type

Medical

Requirements
Must have
• Use existing logo (attached, other versions available upon request)

Sections for:
Mission statement (draft version attached)
Educational Programs: there is only one at the moment, but we will need the option to add more
Faculty members/resident staff (contact database); webform to apply to join
Events calendar/list
Emphasis on search engine optimization
Nice to have
• News/publication tabs for the front page (similar to those on http://www.trelvo.halvorsen.edu/)

It would be helpful if you could use the Halvorsen color palette: http://www.halvorsen.edu/webservices/styleguide/color.html

```html
<!DOCTYPE html>
<html lang="en">
<head>
<meta charset="utf-8">
<title>Center for Cellular Datacraft</title>
<link href="https://fonts.googleapis.com/css2?family=PT+Sans+Narrow&family=Source+Sans+3:wght@400;600&family=Arimo&display=swap" rel="stylesheet">
<style>
:root{
  --navy:#0b1a5c;
  --blue:#1b3aa8;
  --blue-dark:#0e2a8c;
  --link:#1f3aa0;
  --title:#22317a;
  --red:#c0392b;
  --text:#333;
  --muted:#666;
  --rule:#bbb;
  --btn:#e4e4e4;
}
*{margin:0;padding:0;box-sizing:border-box}
html,body{width:1200px;height:1021px;overflow:hidden;background:var(--navy)}
.stage{position:relative;width:1300px;height:1106px;transform:scale(0.923077);transform-origin:0 0;font-family:"Source Sans 3",sans-serif;color:var(--text)}
.abs{position:absolute}
.page{left:166px;top:0;width:968px;height:1020px;background:#fff}
.header{left:166px;top:0;width:968px;height:88px;background:linear-gradient(#fff,#f1f1f1)}
.brand{left:182px;top:16px;display:flex;align-items:center;gap:8px}
.brand-dot{width:48px;height:48px;border-radius:50%;background:var(--title)}
.brand-name{font-size:25px;line-height:25px;color:var(--title);font-weight:400}
.search{left:960px;top:11px;width:163px;height:28px;background:#ececec;border:1px solid #d6d6d6;font-size:12px;padding:6px 10px;color:#444}
.search svg{position:absolute;right:5px;top:5px}
.nav{right:180px;top:57px;display:flex;font-size:14.5px;white-space:nowrap}
.nav a{color:var(--title);text-decoration:none;padding:0 10px;border-left:1px solid #ccc;line-height:20px}
.nav a:first-child{border-left:0;color:var(--red)}
.nav a:last-child{padding-right:0}
.box{border:1px solid #ddd;background:#fff}
.slider{left:184px;top:103px;width:668px;height:353px;background:linear-gradient(110deg,#c9d3dc,#eef1f4 45%,#b7c3cf);}
.arrow{width:50px;height:50px;border-radius:50%;background:rgba(20,40,110,.8);display:flex;align-items:center;justify-content:center}
.caption{left:190px;top:409px;width:656px;height:41px;background:rgba(40,40,40,.55);color:#fff;font-family:"PT Sans Narrow",sans-serif;font-style:italic;font-size:20.5px;line-height:41px;padding:0 10px;white-space:nowrap;overflow:hidden}
.bar{background:linear-gradient(90deg,var(--blue-dark),var(--blue));color:#fff;font-family:"PT Sans Narrow",sans-serif;font-size:20px;padding:6px 8px;box-shadow:0 8px 6px -6px rgba(0,0,0,.45)}
.edu{left:879px;width:240px}
.edu .thumb{position:absolute;left:0;top:0;width:48px;height:52px;background:linear-gradient(135deg,#6a7b5a,#b39a7a)}
.edu .date{position:absolute;left:60px;top:0;font-size:14px;color:#222;white-space:nowrap}
.edu .ttl{position:absolute;left:60px;top:19px;font-family:"PT Sans Narrow",sans-serif;font-size:18px;color:var(--blue);white-space:nowrap}
.edu .meta{position:absolute;left:61px;top:42px;font-size:11px;color:#666;white-space:nowrap}
.dots{border-top:1px dotted #999}
.ev{left:192px;width:216px;font-size:15px;color:var(--blue);line-height:18px}
.ev small{display:block;font-size:12.5px;color:#444}
.btn{background:var(--btn);font-size:13px;color:#444;padding:3px 5px;height:24px;white-space:nowrap}
.li{left:196px;width:212px;font-size:13.5px;color:var(--title)}
.li:before{content:"";display:inline-block;border-left:4px solid var(--title);border-top:3px solid transparent;border-bottom:3px solid transparent;margin-right:12px;vertical-align:1px}
.tab{font-family:"PT Sans Narrow",sans-serif;font-size:18px;color:var(--blue);padding:8px 0;text-align:center}
.news-photo{left:436px;top:528px;width:412px;height:194px;background:linear-gradient(90deg,#8a6b3a,#c7a56b 40%,#4a3a28)}
.news-cap{left:436px;top:664px;width:310px;height:54px;background:rgba(0,0,0,.7);color:#fff;font-family:Arimo,sans-serif;font-size:14px;line-height:16px;text-align:center;padding:2px 4px}
.nl{left:437px;width:415px;font-size:12.5px;color:var(--link);line-height:18px}
.more{left:438px;top:964px;font-size:13px;font-weight:600;color:var(--blue)}
.person{left:871px;width:244px;height:90px}
.person .ph{position:absolute;left:0;top:0;width:86px;height:84px;border:1px solid #ccc;background:linear-gradient(135deg,#d8dde2,#8fa0b0)}
.person .nm{position:absolute;left:100px;top:5px;font-family:"PT Sans Narrow",sans-serif;font-size:19px;color:var(--blue);white-space:nowrap}
.person .role{position:absolute;left:100px;top:29px;font-family:"PT Sans Narrow",sans-serif;font-size:18px;color:#444}
.person .btn{position:absolute;left:101px;top:57px}
.footer{font-size:12px;color:#fff}
.social{width:26px;height:26px;border-radius:3px}
</style>
</head>
<body>
<div class="stage">
  <div class="abs page"></div>
  <header class="abs header"></header>
  <div class="abs brand"><span class="brand-dot"></span><div class="brand-name">Center for<br>Cellular Datacraft</div></div>
  <div class="abs search">Search<svg width="18" height="18" viewBox="0 0 18 18"><circle cx="7" cy="7" r="5" fill="none" stroke="#888" stroke-width="2"/><line x1="11" y1="11" x2="16" y2="16" stroke="#888" stroke-width="3"/></svg></div>
  <nav class="abs nav"><a>HOME</a><a>ABOUT US</a><a>PROGRAMS</a><a>RESOURCES</a><a>NEWS</a><a>CONTACT US</a></nav>

  <div class="abs box" style="left:179px;top:98px;width:679px;height:364px"></div>
  <div class="abs slider" role="img" aria-label="Lab researcher handling glass flasks with blue liquid"></div>
  <div class="abs arrow" style="left:191px;top:255px"><svg width="20" height="26"><polyline points="15,3 5,13 15,23" fill="none" stroke="#fff" stroke-width="4"/></svg></div>
  <div class="abs arrow" style="left:790px;top:255px"><svg width="20" height="26"><polyline points="5,3 15,13 5,23" fill="none" stroke="#fff" stroke-width="4"/></svg></div>
  <div class="abs caption">This will avoid undesired overlap in expenditures, and facilitate coordination of efforts.</div>

  <div class="abs box" style="left:866px;top:98px;width:258px;height:364px"></div>
  <div class="abs bar" style="left:874px;top:105px;width:244px;height:36px">EDUCATIONAL PROGRAMS</div>
  <div class="abs edu" style="top:161px"><div class="thumb" role="img" aria-label="Students group photo"></div><div class="date">Saturday, March 16, 2013</div><div class="ttl">"Bridge Contest"</div><div class="meta">8:30 a.m., Science Learning Center</div></div>
  <div class="abs dots" style="left:879px;top:227px;width:234px"></div>
  <div class="abs edu" style="top:238px"><div class="thumb" role="img" aria-label="Competition participants"></div><div class="date">Wednesday, March 20, 2013</div><div class="ttl">"MAGLEV Competition"</div><div class="meta">8:30 a.m., Science Learning Center</div></div>
  <div class="abs dots" style="left:879px;top:306px;width:234px"></div>
  <div class="abs edu" style="top:317px"><div class="thumb" role="img" aria-label="Contest participants"></div><div class="date">Wednesday, March 20, 2013</div><div class="ttl">"MAGLEV Contest"</div><div class="meta">8:30 a.m., Science Learning Center</div></div>
  <div class="abs" style="left:874px;top:385px;width:244px;height:70px;background:#eee"></div>
  <div class="abs edu" style="top:393px"><div class="thumb" role="img" aria-label="Science fair participant"></div><div class="date">Saturday, March 16, 2013</div><div class="ttl">"Science Fair"</div><div class="meta">8:30 a.m., Science Learning Center</div></div>

  <div class="abs box" style="left:180px;top:470px;width:944px;height:538px"></div>
  <div class="abs bar" style="left:190px;top:482px;width:217px;height:36px">EVENTS CALENDAR</div>
  <div class="abs ev" style="top:532px">2013 TRELVO SYMPOSIUM<small>Details and registration click here</small></div>
  <div class="abs dots" style="left:190px;top:576px;width:219px"></div>
  <div class="abs ev" style="top:584px">8th Annual International TRELVO Symposium</div>
  <div class="abs dots" style="left:190px;top:630px;width:219px"></div>
  <div class="abs ev" style="top:639px">Harnessing the Paradox: Personalization and the Science of Scale</div>
  <div class="abs dots" style="left:190px;top:701px;width:219px"></div>
  <div class="abs ev" style="top:709px">TRELVO SYMPOSIUM AGENDA 2013</div>
  <div class="abs btn" style="left:193px;top:736px">VIEW MORE</div>
  <div class="abs bar" style="left:190px;top:782px;width:217px;height:36px">LIST</div>
  <div class="abs li" style="top:841px">QR4N Seminar Series</div>
  <div class="abs dots" style="left:190px;top:869px;width:219px"></div>
  <div class="abs li" style="top:881px">TRELVO Seminar Series</div>
  <div class="abs dots" style="left:190px;top:909px;width:219px"></div>
  <div class="abs li" style="top:921px">TRELVO Seminar Series</div>
  <div class="abs dots" style="left:190px;top:950px;width:219px"></div>
  <div class="abs li" style="top:961px">TRELVO Seminar Series</div>

  <div class="abs tab" style="left:439px;top:481px;width:94px;height:35px;background:#e6e6e6">NEWS</div>
  <div class="abs tab" style="left:548px;top:481px;width:90px">PUBLICATIONS</div>
  <div class="abs box" style="left:425px;top:515px;width:434px;height:483px"></div>
  <div class="abs news-photo" role="img" aria-label="Researcher standing in front of laboratory shelves"></div>
  <div class="abs news-cap">IL-2 induces a WAVE2-dependent pathway for actin reorganization that enables WASp-independent human NK cell function</div>
  <div class="abs nl" style="top:738px">Is This The End Of A Widely Used Heart Drug?</div>
  <div class="abs nl" style="top:767px">Halvorsen Medicine at the 2013 Continental College of Heart Medicine Annual Scientific Sessions</div>
  <div class="abs nl" style="top:814px">New Research Shows that While Niacin Added to Statin Therapy Increases HDL Cholesterol Levels It Does Not Improve HDL Functionality</div>
  <div class="abs nl" style="top:865px">Fixing a Broken Drug Business by Spreading the Wealth</div>
  <div class="abs nl" style="top:899px">Heart Research Hits Close to Home for a New Halvorsen Med Prof</div>
  <div class="abs nl" style="top:932px">Taking a Harder Look at Fracking and Health</div>
  <div class="abs more">READ MORE NEWS »</div>

  <div class="abs bar" style="left:871px;top:482px;width:244px;height:36px">FACULTY MEMBERS</div>
  <div class="abs person" style="top:537px"><div class="ph" role="img" aria-label="Faculty member portrait"></div><div class="nm">DANIEL ORSETTI</div><div class="role">STAFF</div><div class="btn">VIEW MORE</div></div>
  <div class="abs dots" style="left:871px;top:633px;width:240px"></div>
  <div class="abs person" style="top:644px"><div class="ph" role="img" aria-label="Faculty member in lab protective gear"></div><div class="nm">TOBIAS</div><div class="role">STAFF</div><div class="btn">VIEW MORE</div></div>
  <div class="abs bar" style="left:871px;top:755px;width:244px;height:36px">RESIDENT STAFF</div>
  <div class="abs person" style="top:805px"><div class="ph" role="img" aria-label="Resident staff portrait"></div><div class="nm">DANIEL ORSETTI</div><div class="role">STAFF</div><div class="btn">VIEW MORE</div></div>
  <div class="abs dots" style="left:871px;top:901px;width:240px"></div>
  <div class="abs person" style="top:914px"><div class="ph" role="img" aria-label="Resident staff member with safety glasses"></div><div class="nm">TOBIAS</div><div class="role">STAFF</div><div class="btn">VIEW MORE</div></div>

  <div class="abs footer" style="left:168px;top:1039px">Follow us On</div>
  <div class="abs" style="left:170px;top:1066px;display:flex;gap:6px">
    <span class="social" style="background:#3b5b9a"></span><span class="social" style="background:#e8731e"></span><span class="social" style="background:#35a6dc"></span><span class="social" style="background:#1e74b0"></span>
  </div>
  <div class="abs footer" style="right:166px;top:1040px;text-align:right;line-height:18px">Home &nbsp;|&nbsp; About Us &nbsp;|&nbsp; Programs &nbsp;|&nbsp; Resources &nbsp;|&nbsp; News &nbsp;|&nbsp; Contact us<br>Copyrights @ 2013 All Rights Reserved</div>
</div>
</body>
</html>
```